Emergency Management Consulting Needs a Website

Need to develop a website for an Emergency Management Consulting business. This website needs to be user friendly and resemble disaster preparedness, response, recovery, and mitigation. It must allow for me to make changes to it myself by adding pages, content and pictures. Looking for an advanced page to the website that allows monitoring of social media sites, hashtags, and keywords. Must have pictures of disasters on the site. Must try to integrate the logo colors, not excessive.

Reason: Did not receive anything sufficient to what I am looking for.

Industry/Entity Type

Government

Coding

Coded - Design and coding required

Number of Pages Required

5+ page

Requirements
Must have
• Logo, advanced social media monitoring page, allow for edits myself (content, pages, graphics) this must be a CMS of some sort, use logo color scheme (not excessively), must be professional looking, connect with Pexaro Domain, find a hosting site, SEO, no "long" designs, minimize "dead" space, no social media feeds, no newsletter stuff.
• Menu items: Home, About Us, Services, Situation Monitor, Work With Us, Contact Us (hopefully these could be editable if I need to later)
• When you make a submission, please send me a message on which CMS you are using. Thank you.
Nice to have
• Examples of websites:
• https://www.qarl.vic.gov.au/
• http://www.malvecorish.com/
• http://www.tuvrakol.org/
• http://pomvaleconsulting.com/
• http://www.sultavon.com/services/emergency-management
• https://uzo.com/
• http://www.velumbra.com/Responsibility/Sustainable-Development/HSE/Crisis-and-Emergency-Management/

```html
<!DOCTYPE html>
<html lang="en">
<head>
<meta charset="utf-8">
<title>Safe. Secure. Resilient. – Featured News</title>
<link href="https://fonts.googleapis.com/css2?family=Montserrat:wght@400;500;700;800&display=swap" rel="stylesheet">
<style>
  :root {
    --red: #e3302f;
    --dark: #2a2a2a;
    --white: #ffffff;
    --black: #0d0d0d;
    --track: #d9d9d9;
  }
  * { box-sizing: border-box; margin: 0; padding: 0; }
  html, body { width: 1200px; height: 1075px; overflow: hidden; background: var(--white); }
  body { position: relative; font-family: "Montserrat", Arial, sans-serif; color: var(--white); }

  .hero { position: absolute; top: 12px; left: 0; width: 1200px; height: 435px; display: flex; }
  .hero-photo { width: 630px; height: 100%; background: linear-gradient(160deg, #3f4a2e 0%, #6e6446 35%, #9c8a66 65%, #b7a27c 100%); }
  .hero-panel { flex: 1; background: var(--red); padding: 86px 0 0 48px; }
  .hero-title { font-weight: 800; font-size: 34px; line-height: 39px; letter-spacing: 0.5px; text-transform: uppercase; }
  .hero-text { margin-top: 40px; width: 390px; font-size: 13.3px; line-height: 16.5px; letter-spacing: 0.4px; font-weight: 500; }
  .btn { display: inline-flex; align-items: center; justify-content: center; background: var(--dark); color: var(--white); font-weight: 700; border-radius: 20px; text-decoration: none; }
  .hero .btn { margin-top: 38px; width: 143px; height: 38px; font-size: 14px; }

  .news-title { position: absolute; top: 502px; left: 0; width: 1200px; text-align: center; font-weight: 800; font-size: 35px; color: var(--black); letter-spacing: -0.3px; }
  .news-title span { color: var(--red); }

  .news-card { position: absolute; top: 587px; width: 294px; height: 392px; background: var(--red); }
  .news-card:nth-of-type(1) { left: 132px; }
  .news-card:nth-of-type(2) { left: 454px; }
  .news-card:nth-of-type(3) { left: 774px; }
  .card-photo { height: 183px; }
  .photo-aircraft { background: linear-gradient(180deg, #9aa2ab 0%, #b9b4a8 55%, #8a7a55 100%); }
  .photo-crew { background: linear-gradient(180deg, #b8423a 0%, #4a4a45 50%, #6f7a3d 100%); }
  .photo-lifeguard { background: linear-gradient(120deg, #3d5535 0%, #7b8a70 45%, #d8b43a 80%, #c9363a 100%); }

  .progress { position: absolute; top: 166px; left: 23px; width: 245px; height: 33px; background: var(--white); border-radius: 17px; display: flex; align-items: center; padding: 0 6px 0 14px; }
  .progress-track { flex: 1; height: 5px; background: var(--track); border-radius: 3px; overflow: hidden; }
  .progress-fill { width: 40%; height: 100%; background: var(--red); }
  .progress-value { margin-left: 6px; font-size: 12px; color: var(--black); font-weight: 500; }

  .card-meta { display: flex; justify-content: space-between; padding: 42px 21px 0; font-size: 12px; font-weight: 700; letter-spacing: 0.3px; }
  .card-heading { margin: 22px auto 0; width: 230px; height: 68px; text-align: center; font-size: 16px; line-height: 19.5px; font-weight: 800; letter-spacing: 0.6px; }
  .card-action { text-align: center; margin-top: 5px; }
  .card-action .btn { width: 125px; height: 32px; font-size: 12px; letter-spacing: 0.3px; }

  .footer-rule { position: absolute; bottom: 0; left: 0; width: 1200px; height: 2px; background: var(--red); }
</style>
</head>
<body>
  <section class="hero">
    <div class="hero-photo" role="img" aria-label="Rescuers in a small boat on a flooded street beside submerged cars"></div>
    <div class="hero-panel">
      <h1 class="hero-title">Safe. Secure.<br>Resilient.</h1>
      <p class="hero-text">Lorem ipsum dolor sit amet, consectetur adipisicing elit, sed do eiusmod tempor iont incididunt ut labore et dolore magna aliqua. Ut enim ad minim veniam, quis nostrudti exercitation ullamco laboris nisi ut aliquip ex ea commodo consequat.</p>
      <a class="btn" href="#">Learn More</a>
    </div>
  </section>

  <h2 class="news-title">FEATURED <span>NEWS</span></h2>

  <article class="news-card">
    <div class="card-photo photo-aircraft" role="img" aria-label="Orange firefighting helicopter on an airfield"></div>
    <div class="progress"><div class="progress-track"><div class="progress-fill"></div></div><span class="progress-value">30%</span></div>
    <div class="card-meta"><span>March 15, 2017</span><span>Goal: $800,000</span></div>
    <h3 class="card-heading">Aircraft a critical component to fighting fires</h3>
    <div class="card-action"><a class="btn" href="#">Read More</a></div>
  </article>

  <article class="news-card">
    <div class="card-photo photo-crew" role="img" aria-label="Emergency crews standing in front of a fire truck"></div>
    <div class="progress"><div class="progress-track"><div class="progress-fill"></div></div><span class="progress-value">30%</span></div>
    <div class="card-meta"><span>March 14, 2017</span><span>Goal: $800,000</span></div>
    <h3 class="card-heading">Victoria’s all emergencies summer season</h3>
    <div class="card-action"><a class="btn" href="#">Read More</a></div>
  </article>

  <article class="news-card">
    <div class="card-photo photo-lifeguard" role="img" aria-label="Lifeguard in a red cap watching over a pool"></div>
    <div class="progress"><div class="progress-track"><div class="progress-fill"></div></div><span class="progress-value">30%</span></div>
    <div class="card-meta"><span>March 13, 2017</span><span>Goal: $800,000</span></div>
    <h3 class="card-heading">Drowning Death Spike</h3>
    <div class="card-action"><a class="btn" href="#">Read More</a></div>
  </article>

  <div class="footer-rule"></div>
</body>
</html>
```